ultra-minimalist business card

front (black background, matte):

tarik b. hosseny
writer | photographer
get@tarikhosseny.com

back (white background, matte):

a picture speaks a thousand words;
a word draws a thousand pictures.

www.tarikhosseny.com

all text should be small (white or silver - as long as it shows against the black - on the front; black or gray - as long as it shows against the white - on the back).

feel free to get creative in terms of arrangement, alignment, and font type, but remember, the overall style is minimalist, so nothing too fancy, please.

thanks.

```html
<!DOCTYPE html>
<html lang="en">
<head>
<meta charset="utf-8">
<title>Tarik B. Hosseny — Business Card</title>
<link rel="stylesheet" href="https://fonts.googleapis.com/css2?family=Titillium+Web:ital,wght@0,300;0,400;0,600;1,300&display=swap">
<style>
  :root {
    --backdrop: #e4e4e6;
    --card-white: #f4f4f5;
    --card-black-deep: #161616;
    --card-black-light: #5c5c5c;
    --ink-gray: #6e6e70;
    --ink-gray-soft: #8c8c8e;
    --ink-silver: #c9c9cb;
    --ink-silver-dim: #9a9a9c;
  }
  * { margin: 0; padding: 0; box-sizing: border-box; }
  html, body {
    width: 1200px;
    height: 720px;
    overflow: hidden;
    background: var(--backdrop);
    font-family: "Titillium Web", "Helvetica Neue", Arial, sans-serif;
  }
  .card-sheet {
    width: 1200px;
    height: 720px;
    display: flex;
    align-items: center;
    justify-content: center;
    gap: 40px;
  }
  .card {
    position: relative;
    width: 540px;
    height: 309px;
    box-shadow: 0 2px 6px rgba(0,0,0,0.12);
  }

  /* Back side */
  .card--back {
    background: var(--card-white);
    display: flex;
    flex-direction: column;
    align-items: center;
    justify-content: center;
    text-align: center;
  }
  .card__quote {
    font-weight: 600;
    font-size: 10.5px;
    letter-spacing: 1.4px;
    text-transform: uppercase;
    color: var(--ink-gray);
    white-space: nowrap;
  }
  .card__website {
    margin-top: 4px;
    font-weight: 400;
    font-size: 8.5px;
    letter-spacing: 2px;
    text-transform: uppercase;
    color: var(--ink-gray-soft);
  }

  /* Front side */
  .card--front {
    background: linear-gradient(200deg, var(--card-black-light) 0%, #2e2e2e 45%, var(--card-black-deep) 100%);
  }
  .card__identity {
    position: absolute;
    left: 34px;
    bottom: 50px;
  }
  .card__name-row {
    display: flex;
    align-items: flex-start;
  }
  .card__name {
    font-weight: 300;
    font-size: 34px;
    line-height: 1;
    letter-spacing: 3px;
    text-transform: uppercase;
    color: var(--ink-silver);
  }
  .card__role {
    margin-left: 6px;
    margin-top: 1px;
    font-style: italic;
    font-weight: 300;
    font-size: 9px;
    letter-spacing: 1px;
    color: var(--ink-silver-dim);
    white-space: nowrap;
  }
  .card__email {
    margin-top: 3px;
    font-weight: 300;
    font-size: 9.5px;
    letter-spacing: 0.8px;
    color: var(--ink-silver-dim);
  }
</style>
</head>
<body>
  <main class="card-sheet">
    <section class="card card--back" aria-label="Card back">
      <p class="card__quote">“A picture speaks a thousand words, a word draws a thousand pictures.”</p>
      <p class="card__website">www.tarikhosseny.com</p>
    </section>

    <section class="card card--front" aria-label="Card front">
      <div class="card__identity">
        <div class="card__name-row">
          <h1 class="card__name">Tarik B. Hosseny</h1>
          <span class="card__role">writer | photographer</span>
        </div>
        <p class="card__email">get@tarikhosseny.com</p>
      </div>
    </section>
  </main>
</body>
</html>
```